依頼詳細
・デザイン概要
今回は、トップページデザインの募集になります。
レスポンシブデザインのサイトで、bootstrap4を利用しコーディングする予定になります。
デザイン幅は2000px、コンテンツの幅はbootstrap4デフォルトの1110pxを基準としてください。ただし最近のデザインの流行を取りいれて、フルワイドや、1200~15000px程度の幅のコンテンツをバランスよくレイアウトしてください。
コンテンツ配置は基本12分割になります。がデザインによっては、多少逸脱してもかまいません。
(12分割のコンテンツ幅については添付のPSDを参考にご覧ください)

本文のフォントはゴシック系は游ゴシック、メイリオ、明朝系は遊明朝でお願いします。
飾り文字はフリーフォントか、googleフォントを利用してください。

メイン画像部分・グローバルメニューは、ワイド適用でお願いします。

掲載画像については、基本は添付ファイルを使用してください。
また、雰囲気が合っていれば、指定外の画像を追加掲載いただいてOKです。

・その他
デザイン・ムード、参考サイトについてなど、掲載内容詳細に関しては、別添のExcel資料を参照してください。

資料上はサイト名(社名)や住所などは伏字にしております。ご提案時点ではそのまま作成をお願いします。当選確定後、本内容に修正をお願いいたします。

当選の方は、希望があれば引き続き下層ページの作成及びコーディング作業を依頼可能です。
ページ数
1ページ
希望イメージ
シンプル 複雑
単色 カラフル
暗い 明るい
日常 高級
遊び心 厳粛
未来的 伝統的
女性的 男性的
希望する色
青系
納品ファイル
• 高解像度JPG (.jpg)
• フォトショップ形式 (.psd)

クライアントと折衝しまして、norvikaplane様のデザインが一番「落ち着いてる雰囲気」と「町工場な印象」を感じたとのことで、当選とさせていただきました。

本件、多数のご提案ありがとうございました。
どの提案もとてもよく、クライアントもかなり悩んでいましたがら、最終的にムードや印象の部分でnorvikaplane様を当選とさせていいただきました。
どうもありがとうございました。
今後とも宜しくお願いいたします。

```html
<!DOCTYPE html>
<html lang="ja">
<head>
<meta charset="utf-8">
<title>有限会社〇〇〇〇製作所</title>
<link rel="stylesheet" href="https://fonts.googleapis.com/css2?family=Noto+Sans+JP:wght@400;500;700&family=Roboto:wght@400;500;700&display=swap">
<style>
:root{
  --navy:#1f4a8e;
  --navy-dark:#173a73;
  --blue-pill:#2a5aa8;
  --accent:#f2d21b;
  --white:#ffffff;
  --ink:#333333;
  --muted:#777777;
  --line:#dddddd;
  --photo-steel:linear-gradient(120deg,#e9e9e9 0%,#9c9c9c 35%,#dcdcdc 55%,#6f6f6f 80%,#cfcfcf 100%);
  --photo-coil:linear-gradient(110deg,#d8d8d8 0%,#8a8a8a 30%,#efefef 50%,#9b9b9b 75%,#e2e2e2 100%);
  --photo-wire:linear-gradient(135deg,#6f8fb8 0%,#3b5d8e 50%,#a9bed6 100%);
}
*{margin:0;padding:0;box-sizing:border-box}
html,body{width:1200px;height:2256px;overflow:hidden}
body{font-family:"Noto Sans JP",sans-serif;color:var(--ink);background:var(--white);position:relative}

/* header + hero */
.hero{position:absolute;left:0;top:0;width:1200px;height:680px}
.hero__photo{position:absolute;inset:0;
  background:
    radial-gradient(ellipse 260px 140px at 560px 440px,rgba(32,84,170,.85),transparent 70%),
    radial-gradient(ellipse 300px 160px at 220px 520px,rgba(40,96,180,.8),transparent 70%),
    radial-gradient(ellipse 160px 90px at 830px 370px,rgba(200,120,50,.7),transparent 70%),
    radial-gradient(ellipse 240px 120px at 950px 180px,rgba(235,240,245,.9),transparent 70%),
    radial-gradient(ellipse 260px 120px at 380px 190px,rgba(230,236,242,.85),transparent 70%),
    radial-gradient(ellipse 220px 200px at 1080px 470px,rgba(50,56,60,.7),transparent 70%),
    linear-gradient(180deg,#8d98a2 0%,#a7b0b6 30%,#6c7880 60%,#4f5a62 100%);}
.site-header{position:absolute;left:0;top:0;width:1200px;height:64px;display:flex;align-items:center;padding:0 24px;background:linear-gradient(180deg,rgba(0,0,0,.25),transparent)}
.site-header__logo{color:var(--white);font-size:13px;font-weight:700;line-height:1.3;width:150px}
.site-header__logo small{display:block;font-size:10px;font-weight:400}
.global-nav{display:flex;gap:34px;margin-left:170px;margin-top:20px}
.global-nav a{color:var(--white);font-size:11px;text-decoration:none}
.tel{margin-left:auto;display:flex;gap:8px;align-self:flex-start;margin-top:12px}
.tel__pill{display:flex;align-items:center;gap:6px;background:var(--blue-pill);color:var(--white);font-family:"Roboto",sans-serif;font-size:13px;font-weight:500;padding:6px 14px;border-radius:16px}
.tel__pill svg{width:12px;height:12px}

/* intro band */
.intro{position:absolute;left:0;top:680px;width:1200px;height:380px;background:var(--navy);overflow:hidden}
.intro__bg-word{position:absolute;left:700px;top:140px;font-family:"Roboto",sans-serif;font-size:90px;font-weight:700;color:rgba(255,255,255,.08);letter-spacing:2px}
.intro__text{position:absolute;left:176px;top:190px;width:840px;color:var(--white);font-size:14px;line-height:2.15}

/* feature sections */
.feature{position:absolute;left:0;width:1200px}
.feature__photo{position:absolute}
.card{position:absolute;background:var(--navy);color:var(--white);padding:40px 40px 0;overflow:hidden}
.card__head{position:relative;height:52px}
.card__title{font-size:22px;font-weight:700;padding-left:16px;border-left:5px solid var(--accent);line-height:1.2}
.card__en{position:absolute;font-family:"Roboto",sans-serif;font-size:38px;font-weight:500;color:rgba(255,255,255,.28);top:8px;letter-spacing:1px;white-space:nowrap}
.card__lead{font-size:15px;font-weight:700;margin-top:12px;display:flex;align-items:center;gap:8px}
.card__lead svg{width:16px;height:16px}
.card__body{font-size:11px;line-height:1.9;margin-top:14px}
.btn-more{display:block;width:240px;margin:22px auto 0;background:var(--white);color:var(--navy);text-align:center;font-family:"Roboto",sans-serif;font-size:13px;font-weight:500;padding:6px 0;border:1px solid var(--white)}

.feature--tech{top:1060px;height:372px}
.feature--tech .feature__photo{left:480px;top:0;width:720px;height:372px;background:var(--photo-steel)}
.feature--tech .card{left:72px;top:56px;width:488px;height:300px}
.feature--tech .card__en{right:0}

.feature--products{top:1452px;height:372px}
.feature--products .feature__photo{left:0;top:0;width:760px;height:372px;background:var(--photo-coil)}
.feature--products .card{left:592px;top:62px;width:536px;height:300px}
.feature--products .card__en{right:0}

/* company + map */
.company{position:absolute;left:0;top:1848px;width:1200px;height:312px}
.company__photo{position:absolute;left:0;top:0;width:380px;height:312px;background:var(--photo-wire)}
.company__box{position:absolute;left:0;top:0;width:380px;height:312px;padding:36px 40px;color:var(--white)}
.company__box .card__en{left:120px;top:44px}
.company__box .card__body{margin-top:22px}
.company__box .btn-more{width:200px}
.map{position:absolute;left:440px;top:0;width:744px;height:312px;background:#eeeeee;display:flex;align-items:center;justify-content:center;color:var(--muted);font-size:13px}

/* footer */
.site-footer{position:absolute;left:0;top:2160px;width:1200px;height:96px;border-top:1px solid var(--line);padding:22px 24px 0}
.site-footer__logo{font-size:13px;font-weight:700;color:var(--ink)}
.site-footer__logo span{font-family:"Roboto",sans-serif;font-size:10px;font-weight:400;color:var(--muted);margin-left:10px}
.site-footer__addr{font-size:10px;color:var(--muted);margin-top:8px}
.footer-nav{position:absolute;right:80px;top:26px;display:flex;gap:30px}
.footer-nav a{font-size:10px;color:var(--ink);text-decoration:none}
.page-top{position:absolute;right:24px;top:44px;width:32px;height:32px;background:var(--navy);display:flex;align-items:center;justify-content:center}
</style>
</head>
<body>

<section class="hero">
  <div class="hero__photo" role="img" aria-label="工場内の作業場、青いコンテナと加工機械が並ぶ様子"></div>
  <header class="site-header">
    <div class="site-header__logo"><small>有限会社</small>〇〇〇〇製作所</div>
    <nav class="global-nav">
      <a href="#">ホーム</a><a href="#">会社概要</a><a href="#">技術紹介</a><a href="#">製品紹介</a><a href="#">設備紹介</a><a href="#">採用情報</a>
    </nav>
    <div class="tel">
      <span class="tel__pill"><svg viewBox="0 0 24 24" fill="#fff"><path d="M6.6 10.8a15 15 0 0 0 6.6 6.6l2.2-2.2a1 1 0 0 1 1-.25 11.4 11.4 0 0 0 3.6.6 1 1 0 0 1 1 1V20a1 1 0 0 1-1 1A17 17 0 0 1 3 4a1 1 0 0 1 1-1h3.5a1 1 0 0 1 1 1c0 1.25.2 2.45.6 3.6a1 1 0 0 1-.25 1z"/></svg>012-345-6789</span>
      <span class="tel__pill"><svg viewBox="0 0 24 24" fill="#fff"><path d="M3 5h18v14H3z M3 5l9 7 9-7" stroke="#2a5aa8" stroke-width="1.5"/></svg>012-345-6789</span>
    </div>
  </header>
</section>

<section class="intro">
  <div class="intro__bg-word">Works</div>
  <p class="intro__text">〇〇〇〇製作所は、金属ばね製品を設計、製作、販売いたします。<br>汎用品、オリジナル品を問わず、精密スプリング、バーコーター、ガードスプリング（ホースガード）、ガイド、専用、特殊、試作品、小ロット品まで幅広く対応いたします。<br>また、サンプル製作、高精度の量産品、細かい加工まで一貫して行っております。どんな事でもご相談ください。<br>お客様のご要望に寄り添うご提案をさせていただきます。</p>
</section>

<section class="feature feature--tech">
  <div class="feature__photo" role="img" aria-label="精密スプリング加工機の部品のクローズアップ"></div>
  <div class="card">
    <div class="card__head"><h2 class="card__title">技術紹介</h2><span class="card__en">Technology</span></div>
    <p class="card__lead"><svg viewBox="0 0 16 16"><path d="M3 8l3 3 7-7" fill="none" stroke="#f2d21b" stroke-width="2.5"/></svg>納得の設計と高い技術力</p>
    <p class="card__body">長年の経験で培った技術とノウハウにて、<br>お客様のご要望にオリジナルのばねを設計・製作いたします。<br>細い線材から太い線材まで対応いたします。</p>
    <a class="btn-more" href="#">MORE</a>
  </div>
</section>

<section class="feature feature--products">
  <div class="feature__photo" role="img" aria-label="金属コイルスプリング製品が並ぶ写真"></div>
  <div class="card">
    <div class="card__head"><h2 class="card__title">製品紹介</h2><span class="card__en">Products</span></div>
    <p class="card__lead"><svg viewBox="0 0 16 16"><path d="M3 8l3 3 7-7" fill="none" stroke="#f2d21b" stroke-width="2.5"/></svg>高精度・高品質な製品加工</p>
    <p class="card__body">厳選された素材で高品質な製品をお届けします。<br>スプリングの製品から特殊な形状まで幅広く対応。<br>汎用品、サンプル品の製作もご相談ください。</p>
    <a class="btn-more" href="#">MORE</a>
  </div>
</section>

<section class="company">
  <div class="company__photo" role="img" aria-label="青みがかった金属線材の写真"></div>
  <div class="company__box">
    <div class="card__head"><h2 class="card__title">会社案内</h2><span class="card__en">Company</span></div>
    <p class="card__body">お客様のご要望に寄り添い、確かな技術で<br>製品をお届けいたします。会社の概要、<br>アクセスについてはこちらをご覧ください。</p>
    <a class="btn-more" href="#">MORE</a>
  </div>
  <div class="map">google mapが埋め込み</div>
</section>

<footer class="site-footer">
  <div class="site-footer__logo">有限会社〇〇〇〇製作所<span>Works</span></div>
  <p class="site-footer__addr">〒000-0000 〇〇県〇〇市〇〇町0-0-0　TEL 012-345-6789</p>
  <nav class="footer-nav">
    <a href="#">ホーム</a><a href="#">会社概要</a><a href="#">技術紹介</a><a href="#">製品紹介</a><a href="#">設備紹介</a><a href="#">採用情報</a><a href="#">お問い合わせ</a>
  </nav>
  <a class="page-top" href="#" aria-label="ページトップへ"><svg width="14" height="14" viewBox="0 0 14 14"><path d="M2 10l5-5 5 5" fill="none" stroke="#fff" stroke-width="2"/></svg></a>
</footer>

</body>
</html>
```